New Townhome community needs for sale sign.

need a 4 foot by 8 foot banner to put on building listing newly constructed townhomes as "coming soon" to market. Construction is scheduled to be completed Dec 2024. Sale of units will begin Spring of 2025.
6 individual townhome units each 2,000 square feet. each unit is 3 bedroom 2.5 bathroom with 2 car garage and each has a rooftop "sky lounge" with amazing views. Gated community. Units available for sale Spring of 2025. Real estate company selling units will be Halvor Realty. Will need Halvor Realty Logo on the banner. Would like to keep with the same blue color scheme as the Halvor Realty logo. phone number on banner to be 602-555-4179. web halvorrealtyx.com.

```html
<!DOCTYPE html>
<html lang="en">
<head>
<meta charset="utf-8">
<title>Coming Soon – Townhome Units Banner</title>
<link rel="stylesheet" href="https://fonts.googleapis.com/css2?family=Montserrat:ital,wght@0,500;0,600;0,800;1,500;1,700&family=Open+Sans:wght@400;700&display=swap">
<style>
  :root {
    --band-blue: #3a88b8;
    --band-blue-light: #5aaed8;
    --sky-blue: #a9cbee;
    --sky-blue-pale: #d6e6f6;
    --accent-blue: #2ba3e3;
    --title-blue: #3b8fd0;
    --stripe-grey: #c9d5e2;
    --stripe-pale: #eef3f9;
    --ink: #3b3f45;
    --navy: #243a55;
    --paper: #ffffff;
    --building-top: #b7a48c;
    --building-mid: #a69683;
    --building-ground: #8c8a89;
  }
  * { margin: 0; padding: 0; box-sizing: border-box; }
  html, body { width: 1200px; height: 723px; overflow: hidden; background: var(--paper); }
  .banner {
    position: relative;
    width: 1200px;
    height: 723px;
    overflow: hidden;
    background: var(--paper);
    font-family: "Open Sans", Arial, sans-serif;
    color: var(--ink);
  }
  .banner-shapes { position: absolute; inset: 0; }
  .headline {
    position: absolute;
    left: 55px;
    top: 62px;
    font-family: "Montserrat", Arial, sans-serif;
    font-weight: 800;
    font-size: 72px;
    line-height: 1;
    letter-spacing: 1px;
    color: var(--paper);
  }
  .sale-label {
    position: absolute;
    left: 55px;
    top: 192px;
    font-family: "Montserrat", Arial, sans-serif;
    font-style: italic;
    font-weight: 500;
    font-size: 46px;
    line-height: 1.2;
    color: var(--title-blue);
  }
  .sale-date {
    position: absolute;
    left: 55px;
    top: 244px;
    font-family: "Montserrat", Arial, sans-serif;
    font-style: italic;
    font-weight: 700;
    font-size: 56px;
    line-height: 1.2;
    color: var(--accent-blue);
  }
  .units-title {
    position: absolute;
    left: 58px;
    top: 336px;
    font-weight: 700;
    font-size: 25px;
    line-height: 1.4;
    color: var(--ink);
  }
  .feature-list {
    position: absolute;
    left: 58px;
    top: 384px;
    list-style: none;
    font-size: 18px;
    line-height: 33px;
    color: var(--ink);
  }
  .feature-list li::before {
    content: "";
    display: inline-block;
    width: 6px;
    height: 6px;
    background: var(--ink);
    margin-right: 12px;
    vertical-align: middle;
  }
  .contact {
    position: absolute;
    left: 98px;
    font-family: "Montserrat", Arial, sans-serif;
    font-weight: 500;
    font-size: 24px;
    line-height: 28px;
    color: var(--ink);
  }
  .contact-phone { top: 588px; }
  .contact-web { top: 634px; }
  .brand {
    position: absolute;
    left: 900px;
    top: 56px;
    display: flex;
    align-items: center;
    gap: 12px;
    font-family: "Montserrat", Arial, sans-serif;
    font-weight: 600;
    font-size: 30px;
    line-height: 1;
    color: var(--navy);
    white-space: nowrap;
  }
  .brand-mark { width: 30px; height: 30px; background: var(--accent-blue); flex: none; }
</style>
</head>
<body>
<main class="banner">
  <svg class="banner-shapes" width="1200" height="723" viewBox="0 0 1200 723" xmlns="http://www.w3.org/2000/svg">
    <defs>
      <linearGradient id="bandGradient" x1="0" y1="0" x2="1" y2="0">
        <stop offset="0" stop-color="var(--band-blue-light)"/>
        <stop offset="1" stop-color="var(--band-blue)"/>
      </linearGradient>
      <linearGradient id="skyGradient" x1="0" y1="0" x2="1" y2="1">
        <stop offset="0" stop-color="var(--sky-blue-pale)"/>
        <stop offset="1" stop-color="var(--sky-blue)"/>
      </linearGradient>
      <linearGradient id="buildingGradient" x1="0" y1="0" x2="0" y2="1">
        <stop offset="0" stop-color="var(--building-top)"/>
        <stop offset="0.7" stop-color="var(--building-mid)"/>
        <stop offset="1" stop-color="var(--building-ground)"/>
      </linearGradient>
      <linearGradient id="fadeGradient" x1="0" y1="0" x2="1" y2="0">
        <stop offset="0" stop-color="var(--stripe-pale)"/>
        <stop offset="1" stop-color="var(--paper)"/>
      </linearGradient>
    </defs>
    <polygon class="sky-panel" points="860,0 1200,0 1200,170 760,170" fill="url(#skyGradient)"/>
    <polygon class="light-stripe" points="740,0 860,0 560,360 440,360" fill="url(#fadeGradient)" opacity="0.9"/>
    <polygon class="sky-stripe" points="960,0 1010,0 870,170 820,170" fill="var(--paper)" opacity="0.8"/>
    <polygon class="header-band" points="0,0 755,0 615,165 0,165" fill="url(#bandGradient)"/>
    <polygon class="grey-stripe" points="270,723 390,723 640,420 540,420" fill="var(--stripe-grey)"/>
    <polygon class="building-photo" points="380,723 845,170 1200,170 1200,723" fill="url(#buildingGradient)" role="img" aria-label="Photo of the new townhome building exterior with garage doors and a paved driveway"/>
    <g class="icon-phone" transform="translate(58,591)">
      <rect width="22" height="22" rx="5" fill="var(--accent-blue)"/>
      <path d="M7 5 l3 0 l1 4 l-2 1 q1 3 4 4 l1 -2 l4 1 l0 3 q-1 2 -3 1 q-8 -3 -10 -10 q-1 -2 1 -2 z" fill="var(--paper)"/>
    </g>
    <g class="icon-web" transform="translate(58,637)">
      <circle cx="11" cy="11" r="11" fill="var(--accent-blue)"/>
      <circle cx="11" cy="11" r="6.5" fill="none" stroke="var(--paper)" stroke-width="1.4"/>
      <ellipse cx="11" cy="11" rx="2.8" ry="6.5" fill="none" stroke="var(--paper)" stroke-width="1.2"/>
      <line x1="4.5" y1="11" x2="17.5" y2="11" stroke="var(--paper)" stroke-width="1.2"/>
    </g>
  </svg>

  <h1 class="headline">COMING SOON</h1>

  <div class="brand">
    <span class="brand-mark"></span>
    <span class="brand-name">Halvor Realty</span>
  </div>

  <p class="sale-label">Units Sale</p>
  <p class="sale-date">Spring 2025</p>

  <h2 class="units-title">6 Individual Townhome Units</h2>
  <ul class="feature-list">
    <li>2,000 Square Feet</li>
    <li>3 Bedroom</li>
    <li>2.5 Bathroom With</li>
    <li>2 Car Garage Rooftop "Sky Lounge"</li>
    <li>Gated Community</li>
  </ul>

  <p class="contact contact-phone">602-555-4179</p>
  <p class="contact contact-web">www.halvorrealtyx.com</p>
</main>
</body>
</html>
```